Roofing Company Sales Rep Business Card

Business card for sales rep to canvass and hand out to property owners/managers for free roof inspections and roof replacements.

```html
<!DOCTYPE html>
<html lang="en">
<head>
<meta charset="UTF-8">
<title>Summit Ridge Roofing – Sales Rep Business Card</title>
<link href="https://fonts.googleapis.com/css2?family=Montserrat:wght@400;500;700&display=swap" rel="stylesheet">
<style>
  :root {
    --bg: #3a3a3a;
    --card-black: #0a0a0a;
    --card-white: #ffffff;
    --accent-red: #e4232b;
    --text-light: #f2f2f2;
    --text-dark: #111111;
  }
  * { margin: 0; padding: 0; box-sizing: border-box; }
  html, body {
    width: 1200px; height: 1200px; overflow: hidden;
    background: var(--bg);
    font-family: "Montserrat", sans-serif;
  }
  .canvas {
    width: 1200px; height: 1200px;
    display: flex; flex-direction: column; align-items: center; justify-content: center;
    gap: 60px;
  }
  .card {
    position: relative;
    width: 860px; height: 500px;
    border-radius: 36px;
    overflow: hidden;
    background: var(--card-black);
  }
  .card-front__split {
    position: absolute; inset: 0; width: 100%; height: 100%;
  }
  .contact {
    position: absolute; left: 70px; top: 200px;
    color: var(--text-light);
  }
  .contact__name {
    color: var(--accent-red);
    font-weight: 500; font-size: 38px; letter-spacing: 0.5px; line-height: 1;
  }
  .contact__position {
    font-size: 22px; font-weight: 400; margin-top: 6px; letter-spacing: 0.5px;
  }
  .contact__list { list-style: none; margin-top: 26px; }
  .contact__item {
    display: flex; align-items: center; gap: 14px;
    font-size: 24px; font-weight: 400; line-height: 1; margin-bottom: 16px;
  }
  .contact__icon { width: 24px; height: 24px; flex: none; }
  .brand {
    position: absolute;
    display: flex; align-items: center; gap: 14px;
    font-weight: 700; text-transform: uppercase; letter-spacing: 1px;
  }
  .brand__mark { display: block; background: var(--accent-red); flex: none; }
  .brand--front {
    left: 540px; top: 0; height: 100%;
    font-size: 32px; color: var(--text-dark); line-height: 1.1;
  }
  .brand--front .brand__mark { width: 22px; height: 22px; }
  .brand--back {
    inset: 0; justify-content: center;
    font-size: 56px; color: var(--text-light);
  }
  .brand--back .brand__mark { width: 36px; height: 36px; }
</style>
</head>
<body>
<main class="canvas">
  <section class="card card-front" aria-label="Business card front">
    <svg class="card-front__split" viewBox="0 0 860 500" preserveAspectRatio="none" aria-hidden="true">
      <polygon points="420,0 860,0 860,500 618,500" fill="var(--card-white)"/>
      <polygon points="408,0 430,0 630,500 608,500" fill="var(--accent-red)"/>
      <polygon points="402,0 408,0 608,500 602,500" fill="var(--card-white)"/>
    </svg>
    <div class="contact">
      <p class="contact__name">FULL NAME</p>
      <p class="contact__position">POSITION</p>
      <ul class="contact__list">
        <li class="contact__item">
          <svg class="contact__icon" viewBox="0 0 24 24" aria-hidden="true"><path fill="var(--accent-red)" d="M6.6 10.8a15.1 15.1 0 0 0 6.6 6.6l2.2-2.2a1 1 0 0 1 1-.25 11.4 11.4 0 0 0 3.6.57 1 1 0 0 1 1 1V20a1 1 0 0 1-1 1A17 17 0 0 1 3 4a1 1 0 0 1 1-1h3.5a1 1 0 0 1 1 1c0 1.25.2 2.45.57 3.57a1 1 0 0 1-.25 1z"/></svg>
          (000) 000 0000
        </li>
        <li class="contact__item">
          <svg class="contact__icon" viewBox="0 0 24 24" aria-hidden="true"><rect x="2" y="5" width="20" height="14" fill="var(--accent-red)"/><path d="M2 5l10 8 10-8" fill="none" stroke="var(--card-black)" stroke-width="2"/></svg>
          email@company.com
        </li>
        <li class="contact__item">
          <svg class="contact__icon" viewBox="0 0 24 24" aria-hidden="true"><g fill="none" stroke="var(--accent-red)" stroke-width="2"><circle cx="12" cy="12" r="10"/><ellipse cx="12" cy="12" rx="4.5" ry="10"/><path d="M2 12h20M4 7h16M4 17h16"/></g></svg>
          www.company.com
        </li>
      </ul>
    </div>
    <div class="brand brand--front">
      <span class="brand__mark"></span>
      <span class="brand__name">Summit Ridge<br>Roofing</span>
    </div>
  </section>

  <section class="card card-back" aria-label="Business card back">
    <div class="brand brand--back">
      <span class="brand__mark"></span>
      <span class="brand__name">Summit Ridge Roofing</span>
    </div>
  </section>
</main>
</body>
</html>
```